Harbinger Slabworks, Inc. Business Card

Create a business card that is eye catching and based around concrete sawcutting. I've attached our current business card and logo for reference. We like aspects of the current business card, but it is starting to feel very loud and lost. We would like something that is still fun but is more modern and streamlined.

```html
<!DOCTYPE html>
<html lang="en">
<head>
<meta charset="utf-8">
<title>Harbinger Slabworks, Inc. Business Card</title>
<link href="https://fonts.googleapis.com/css2?family=Montserrat:wght@500;700&family=Oswald:wght@500&display=swap" rel="stylesheet">
<style>
  :root{
    --stage:#3a3a3c;
    --card-white:#ffffff;
    --card-fog:#f1f1f2;
    --ink:#1b1b1b;
    --red:#d6111f;
    --navy:#1f2a6b;
    --steel-dark:#111113;
    --steel-mid:#2a2a2d;
    --silver:#d8d8d8;
  }
  *{box-sizing:border-box;margin:0;padding:0}
  html,body{width:1200px;height:1200px;overflow:hidden}
  body{background:var(--stage);font-family:"Montserrat",Arial,sans-serif;position:relative}
  .card{position:absolute;left:160px;width:880px;height:503px;border-radius:34px;overflow:hidden;box-shadow:0 18px 40px rgba(0,0,0,.45)}
  .card--front{top:64px;background:linear-gradient(180deg,var(--card-white) 55%,var(--card-fog))}
  .card--back{top:633px;background:radial-gradient(ellipse at 50% 30%,var(--steel-mid),var(--steel-dark) 75%)}

  .flag-wave{position:absolute;left:0;top:0;width:520px;height:330px;
    background:linear-gradient(160deg,rgba(200,210,235,.55) 0%,rgba(240,205,210,.45) 40%,rgba(255,255,255,0) 75%)}

  .brand{position:absolute;display:flex;flex-direction:column;align-items:center;justify-content:center;gap:14px}
  .brand__dot{width:22px;height:22px;border-radius:50%;background:var(--red)}
  .brand__name{font-weight:700;color:var(--navy);text-align:center;letter-spacing:1px;line-height:1.15}
  .card--front .brand{right:70px;top:80px;width:300px;height:240px}
  .card--front .brand__name{font-size:30px}
  .card--back .brand{left:250px;top:40px;width:380px;height:250px}
  .card--back .brand__name{font-size:40px;color:var(--silver)}

  .person{position:absolute;left:70px;top:250px}
  .person__name{font-weight:700;color:var(--red);font-size:34px;letter-spacing:1px}
  .person__role{font-weight:500;color:var(--ink);font-size:18px;letter-spacing:1px;margin-top:2px}
  .contact{list-style:none;margin:20px 0 0 24px}
  .contact li{display:flex;align-items:flex-start;gap:14px;font-size:18px;font-weight:500;color:var(--ink);line-height:1.2;margin-bottom:8px}
  .contact svg{flex:none;width:20px;height:20px;fill:var(--red);margin-top:1px}

  .hotline{position:absolute;left:0;right:0;top:318px;display:flex;justify-content:center;align-items:center;gap:14px;
    font-family:"Oswald",Arial Narrow,sans-serif;font-weight:500;color:#fff;font-size:40px;letter-spacing:1px}
  .hotline svg{width:32px;height:32px;fill:var(--red)}
  .services{position:absolute;left:0;right:0;bottom:52px;display:flex;justify-content:center;align-items:center;gap:20px;
    font-family:"Oswald",Arial Narrow,sans-serif;font-weight:500;color:#e6e6e6;font-size:22px;letter-spacing:1px;text-transform:uppercase}
  .services .sep{width:11px;height:11px;border-radius:50%;background:var(--red)}
</style>
</head>
<body>

<section class="card card--front">
  <div class="flag-wave" role="img" aria-label="Faint waving American flag decoration"></div>
  <div class="brand">
    <span class="brand__dot"></span>
    <span class="brand__name">HARBINGER<br>SLABWORKS</span>
  </div>
  <div class="person">
    <h1 class="person__name">MARISSA KOLE</h1>
    <p class="person__role">OWNER</p>
    <ul class="contact">
      <li><svg viewBox="0 0 24 24"><path d="M6.6 10.8a15 15 0 0 0 6.6 6.6l2.2-2.2a1 1 0 0 1 1-.25 11.4 11.4 0 0 0 3.6.57 1 1 0 0 1 1 1V20a1 1 0 0 1-1 1A17 17 0 0 1 3 4a1 1 0 0 1 1-1h3.5a1 1 0 0 1 1 1c0 1.25.2 2.45.57 3.57a1 1 0 0 1-.25 1z"/></svg>855.555.0142</li>
      <li><svg viewBox="0 0 24 24"><path d="M7 1h10a2 2 0 0 1 2 2v18a2 2 0 0 1-2 2H7a2 2 0 0 1-2-2V3a2 2 0 0 1 2-2zm0 3v14h10V4zm5 15.5a1 1 0 1 0 0 2 1 1 0 0 0 0-2z"/></svg>973.555.0186</li>
      <li><svg viewBox="0 0 24 24"><path d="M2 5h20v14H2zm2 2v.5l8 5 8-5V7l-8 5z"/></svg>marissa@harbingerslabworks.com</li>
      <li><svg viewBox="0 0 24 24"><path d="M12 2a7 7 0 0 0-7 7c0 5 7 13 7 13s7-8 7-13a7 7 0 0 0-7-7zm0 9.5A2.5 2.5 0 1 1 12 6.5a2.5 2.5 0 0 1 0 5z"/></svg><span>48 N. Lantern Ave.<br>Ridgefield, NJ 07657</span></li>
    </ul>
  </div>
</section>

<section class="card card--back" role="img" aria-label="Dark diamond plate steel texture background">
  <div class="brand">
    <span class="brand__dot"></span>
    <span class="brand__name">HARBINGER<br>SLABWORKS</span>
  </div>
  <div class="hotline">
    <svg viewBox="0 0 24 24"><path d="M6.6 10.8a15 15 0 0 0 6.6 6.6l2.2-2.2a1 1 0 0 1 1-.25 11.4 11.4 0 0 0 3.6.57 1 1 0 0 1 1 1V20a1 1 0 0 1-1 1A17 17 0 0 1 3 4a1 1 0 0 1 1-1h3.5a1 1 0 0 1 1 1c0 1.25.2 2.45.57 3.57a1 1 0 0 1-.25 1z"/></svg>
    <span>855-SLAB-CUT</span>
  </div>
  <div class="services">
    <span>Wall Sawing</span><span class="sep"></span>
    <span>Core Drilling</span><span class="sep"></span>
    <span>Slab Sawing</span><span class="sep"></span>
    <span>Breaking &amp; Removal</span>
  </div>
</section>

</body>
</html>
```